Business Card

We need some ideas for corporate business cards. I'm interested in a double sided card, with one side featuring our corporate logo, the other side with employee information.

Corporate colors, logo etc. available at www.brivalo.com

Industry/Entity Type

Business

Requirements
Must have
• The "Brivalo" logo with stylized "O"

Nice to have
• Preferred font is calibri

```html
<!DOCTYPE html>
<html lang="en">
<head>
<meta charset="utf-8">
<title>Brivalo Business Card</title>
<link href="https://fonts.googleapis.com/css2?family=Carlito:wght@400;700&display=swap" rel="stylesheet">
<style>
  :root {
    --crimson: #9c1a47;
    --crimson-dark: #86143c;
    --crimson-light: #a81f4f;
    --paper: #ffffff;
    --ink: #2b2b2b;
    --muted: #6f6f6f;
    --stage: #e9e9eb;
  }
  * { box-sizing: border-box; margin: 0; padding: 0; }
  html, body {
    width: 1200px; height: 900px; overflow: hidden;
    background: var(--stage);
    font-family: "Carlito", "Calibri", sans-serif;
  }
  .sheet {
    width: 1200px; height: 900px;
    display: flex; align-items: center; justify-content: center; gap: 44px;
  }
  .card {
    position: relative;
    width: 540px; height: 330px;
    overflow: hidden;
    box-shadow: 0 6px 18px rgba(0,0,0,0.18);
  }

  /* Front: brand side */
  .card-front {
    background: linear-gradient(135deg, var(--crimson-light), var(--crimson) 55%, var(--crimson-dark));
    color: var(--paper);
  }
  .brand {
    position: absolute; left: 56px; top: 118px;
    display: flex; align-items: center; gap: 16px;
  }
  .brand-mark {
    width: 30px; height: 30px; background: var(--paper);
  }
  .brand-name {
    font-weight: 700; font-size: 72px; letter-spacing: 4px; line-height: 1;
    color: var(--paper);
  }
  .front-url {
    position: absolute; left: 56px; bottom: 42px;
    font-size: 19px; color: var(--paper);
  }

  /* Back: employee side */
  .card-back { background: var(--paper); }
  .person { position: absolute; left: 40px; top: 30px; }
  .person-name {
    font-weight: 700; font-size: 27px; color: var(--crimson); letter-spacing: 0.5px; line-height: 1;
  }
  .person-title { font-size: 17px; color: var(--ink); margin-top: 3px; }
  .company {
    position: absolute; left: 40px; top: 100px;
    font-size: 15.5px; line-height: 1.2; color: var(--muted);
  }
  .contacts {
    position: absolute; left: 40px; top: 178px;
    list-style: none; font-size: 15.5px; line-height: 1.2; color: var(--muted);
  }
  .contacts li { display: flex; align-items: center; gap: 6px; }
  .contacts svg { width: 12px; height: 12px; fill: var(--crimson); flex: none; }
  .back-band { position: absolute; left: 0; bottom: 0; width: 540px; height: 60px; }
  .back-url {
    position: absolute; right: 34px; bottom: 12px;
    font-size: 17px; color: var(--paper);
  }
</style>
</head>
<body>
<main class="sheet">

  <section class="card card-front" aria-label="Card front">
    <div class="brand">
      <span class="brand-mark"></span>
      <span class="brand-name">BRIVALO</span>
    </div>
    <p class="front-url">www.brivalo.com</p>
  </section>

  <section class="card card-back" aria-label="Card back">
    <div class="person">
      <h1 class="person-name">JOHN DOE</h1>
      <p class="person-title">Job title</p>
    </div>
    <address class="company" style="font-style:normal">
      Brivalo<br>
      14 Larchfield Road, Northgate Business Park,<br>
      Dublin 9, Dublin, DB, Ireland
    </address>
    <ul class="contacts">
      <li>
        <svg viewBox="0 0 12 12" aria-hidden="true"><path d="M2.5 0.8l2 2-1 1.4c.6 1.4 1.8 2.7 3.3 3.3l1.4-1 2 2-1.2 1.9C5 10 1.8 6.8 0.6 2z"/></svg>
        +353 1 555 0142
      </li>
      <li>
        <svg viewBox="0 0 12 12" aria-hidden="true"><rect x="3" y="0.5" width="6" height="3.5"/><rect x="0.5" y="4.5" width="11" height="5" rx="1"/><rect x="3" y="8.5" width="6" height="3"/></svg>
        +353 1 555 0187
      </li>
      <li>
        <svg viewBox="0 0 12 12" aria-hidden="true"><path d="M3 0.5h6v11H3z M4 1.8v7.4h4V1.8z"/></svg>
        +000 0 000 0000
      </li>
      <li>
        <svg viewBox="0 0 12 12" aria-hidden="true"><path d="M0.5 2.5h11v7h-11z M1.2 3l4.8 3.6L10.8 3z" fill-rule="evenodd"/></svg>
        name@domainname.com
      </li>
    </ul>
    <svg class="back-band" viewBox="0 0 540 60" aria-hidden="true">
      <line x1="0" y1="22" x2="246" y2="22" stroke="var(--crimson)" stroke-width="2.5"/>
      <polygon points="0,30 250,30 272,12 540,12 540,60 0,60" fill="var(--crimson)"/>
    </svg>
    <p class="back-url">www.brivalo.com</p>
  </section>

</main>
</body>
</html>
```